Electrician Needs A Business Card

I already have a logo and would like a business card to be designed based around this logo the company is called Tolvane Electrical Pty Ltd

The business card will be printed on transparent plastic so I need it to stand out from the crowd. I do not want the card to have anything to do with Electrical on it eg light bulbs, power points etc

I need it to have the following details.

Gareth Pomfrey
Mobile : 0437 519 284
email : gareth@tolvaneelectrical.com.au

If it could incorporate the following onto the bottom of the card
ELECTRICAL - COMMUNICATIONS - AUDIO - VISUAL

```html
<!DOCTYPE html>
<html lang="en">
<head>
<meta charset="utf-8">
<title>Tolvane Electrical – Business Card</title>
<link href="https://fonts.googleapis.com/css2?family=Source+Sans+3:wght@400;600&display=swap" rel="stylesheet">
<style>
  :root {
    --amber: #f5a623;
    --ink: #1d1d1b;
    --card: #efefef;
    --row-grey: #c9cacb;
    --stage: #ffffff;
    --white: #ffffff;
  }
  * { margin: 0; padding: 0; box-sizing: border-box; }
  html, body {
    width: 1200px;
    height: 800px;
    overflow: hidden;
    background: var(--stage);
    font-family: "Source Sans 3", sans-serif;
  }
  .business-card {
    position: absolute;
    left: 150px;
    top: 140px;
    width: 900px;
    height: 520px;
    background: var(--card);
    border-radius: 22px;
    overflow: hidden;
    box-shadow: 0 0 0 1px #dcdcdc;
  }
  .brand {
    position: absolute;
    left: 64px;
    top: 86px;
    display: flex;
    align-items: center;
    gap: 30px;
  }
  .brand-square {
    width: 120px;
    height: 120px;
    background: var(--amber);
  }
  .brand-name {
    font-size: 62px;
    font-weight: 600;
    color: var(--ink);
    letter-spacing: 0.5px;
    white-space: nowrap;
  }
  .contact-band {
    position: absolute;
    left: 0;
    bottom: 0;
    width: 900px;
    height: 193px;
    display: block;
  }
  .band-text { font-family: "Source Sans 3", sans-serif; }
  .holder-name { font-size: 38px; fill: var(--ink); }
  .contact-line { font-size: 20px; fill: var(--ink); }
  .services-line { font-size: 15px; fill: var(--white); letter-spacing: 1px; }
</style>
</head>
<body>
  <div class="business-card">
    <div class="brand">
      <div class="brand-square"></div>
      <div class="brand-name">TOLVANE ELECTRICAL</div>
    </div>

    <svg class="contact-band" viewBox="0 0 900 193" xmlns="http://www.w3.org/2000/svg">
      <rect class="email-row" x="0" y="0" width="900" height="58" fill="var(--row-grey)"/>
      <rect class="mobile-row" x="0" y="64" width="900" height="64" fill="var(--row-grey)"/>
      <rect class="triangle-row" x="0" y="128" width="900" height="29" fill="var(--ink)"/>
      <g class="triangle-marks" fill="var(--amber)">
        <polygon points="560,153 577,131 594,153"/>
        <polygon points="612,153 629,131 646,153"/>
        <polygon points="664,153 681,131 698,153"/>
        <polygon points="716,153 733,131 750,153"/>
        <polygon points="768,153 785,131 802,153"/>
        <polygon points="820,153 837,131 854,153"/>
      </g>
      <polygon class="name-panel" points="0,0 425,0 540,157 0,157" fill="var(--amber)"/>
      <rect class="services-strip" x="0" y="157" width="900" height="36" fill="var(--ink)"/>

      <text class="band-text holder-name" x="85" y="90">Gareth Pomfrey</text>
      <text class="band-text contact-line" x="488" y="37">Email : gareth@tolvaneelectrical.com.au</text>
      <text class="band-text contact-line" x="535" y="103">Mobile : 0437 519 284</text>
      <text class="band-text services-line" x="250" y="181">ELECTRICAL - COMMUNICATIONS - AUDIO - VISUAL</text>
    </svg>
  </div>
</body>
</html>
```